Coral Ridge Networks Ltd

I need a website that is an informational only. We are a construction business building telecommunications sites. Seeing how our company is Coral Ridge the color blue might want to be incorporated in the color scheme.
I can provide more picture of towers and wireless communications if needed.
current website www.coralridgenet.ca

Industry/Entity Type

Wireless Telecommunications, Construction

Coding

Coded - Design and coding required

Number of Pages Required

2 page

Font styles to use
Sans Serif

Colors

Designer to choose colors to be used in the design.

```html
<!DOCTYPE html>
<html lang="en">
<head>
<meta charset="utf-8">
<title>Coral Ridge Networks Ltd</title>
<link href="https://fonts.googleapis.com/css2?family=Lato:wght@400;700;900&family=Montserrat:wght@400;500;600&display=swap" rel="stylesheet">
<style>
:root{
  --navy:#2f4c8c;
  --blue:#3a5ca8;
  --sky:#5db4e4;
  --ink:#1c1c1c;
  --text:#555b66;
  --band:#e9eff8;
  --line:#a9c8ea;
  --white:#ffffff;
}
*{margin:0;padding:0;box-sizing:border-box}
html,body{width:1200px;height:4827px;overflow:hidden;background:var(--white)}
body{position:relative;font-family:"Montserrat",sans-serif;color:var(--text)}
.abs{position:absolute}
h1,h2,h3{font-family:"Lato",sans-serif;color:var(--ink)}
.section-title{position:absolute;left:0;width:1200px;text-align:center;font-size:36px;font-weight:900}

/* nav */
.nav{top:0;left:0;width:1200px;height:88px;background:var(--white)}
.brand{left:109px;top:26px;font-family:"Montserrat",sans-serif;font-size:27px;font-weight:500;color:var(--blue);display:flex;align-items:center;gap:8px}
.brand i{display:block;width:12px;height:12px;border-radius:50%;background:var(--sky)}
.menu{left:438px;top:37px;display:flex;gap:26px;font-size:14px;font-weight:500;color:var(--ink)}
.menu .active{color:var(--sky)}
.phone-btn{left:936px;top:20px;width:161px;height:51px;border:1.5px solid var(--blue);display:flex;align-items:center;justify-content:center;font-size:14px;color:var(--blue)}

/* hero */
.hero{top:88px;left:0;width:1200px;height:615px;background:linear-gradient(100deg,#f1f2f4 0%,#dfe3ea 38%,#9fb7d4 62%,#6f94c4 80%,#c9cdd2 100%)}
.hero h1{left:105px;top:198px;font-size:48px;line-height:77px;font-weight:700;width:640px}
.hero p{left:105px;top:354px;font-size:19px;line-height:30px;color:var(--ink);width:580px}
.btn{display:flex;align-items:center;justify-content:center;background:var(--navy);color:var(--white);font-size:14px;font-weight:600}
.hero .btn{left:105px;top:375px;width:227px;height:51px;top:463px}

/* about */
.about-frame{left:13px;top:800px;width:506px;height:366px;border:2px solid var(--blue);border-left:none;border-bottom:none}
.about-frame::after{content:"";position:absolute;right:-2px;bottom:0;width:2px;height:100%;background:var(--blue)}
.about-photo{left:0;top:812px;width:508px;height:367px;background:linear-gradient(160deg,#6f9fd9 0%,#a9c4e4 35%,#8e9196 65%,#6e6a62 100%)}
.about h2{left:566px;top:835px;font-size:36px;font-weight:900}
.about-copy{left:566px;top:910px;width:524px;font-size:14px;line-height:24px;color:#4a4f58}
.about-copy p{margin-bottom:24px}

/* services */
.service{width:285px}
.service .photo{width:285px;height:223px}
.service h3{margin-top:36px;font-family:"Montserrat",sans-serif;font-size:18px;font-weight:500;color:var(--blue)}
.service p{margin-top:20px;font-size:14px;line-height:24px;color:#5a5f68}
.divider{width:1px;height:422px;top:1382px;background:var(--line)}

/* values */
.values{top:1899px;left:0;width:1200px;height:630px;background:linear-gradient(180deg,#edf2fa 0%,#e3eaf5 60%,#d6dfee 100%)}
.value{width:300px}
.value svg{display:block}
.value h3{margin-top:12px;font-family:"Montserrat",sans-serif;font-size:19px;font-weight:500;color:var(--blue)}
.value p{margin-top:12px;font-size:11.5px;line-height:18px;color:#6a6f78}

/* trusted */
.partner{width:145px;height:92px;border:1.5px solid var(--line);display:flex;align-items:center;justify-content:center;background:var(--white)}
.partner span{display:block;width:96px;height:44px;border-radius:6px;background:linear-gradient(90deg,#c6e53a,#2fcf7b 55%,#2aa6a0)}

/* why */
.why{top:3088px;left:0;width:1200px;height:531px;background:linear-gradient(180deg,#edf2fa 0%,#e2e9f4 100%)}
.why-copy{left:105px;top:3250px;width:990px;text-align:center;font-size:14px;line-height:24px;color:#3d424b}
.check{display:flex;align-items:center;gap:18px;font-size:14px;font-weight:500;color:var(--ink);width:420px;line-height:20px}

/* contact */
.form-frame{left:489px;top:3829px;width:595px;height:499px;border:1.5px solid var(--line)}
.info-card{left:116px;top:3893px;width:432px;height:388px;background:linear-gradient(135deg,#5aa9dd 0%,#3f6fb6 55%,#2f4c8c 100%);color:var(--white)}
.info-card h3{position:absolute;left:62px;top:72px;font-family:"Montserrat",sans-serif;font-size:30px;font-weight:500;color:var(--white)}
.info-row{position:absolute;left:62px;display:flex;align-items:center;gap:22px;font-size:14px}
.form h3{left:645px;top:3898px;font-family:"Montserrat",sans-serif;font-size:28px;font-weight:500}
.field{font-size:14px;color:#4a4f58;border-bottom:1px solid #c8ccd3;height:38px}

/* footer */
.footer{top:4421px;left:0;width:1200px;height:406px}
.foot-col h4{font-family:"Montserrat",sans-serif;font-size:18px;font-weight:600;color:var(--white);margin-bottom:24px}
.foot-col a{display:block;color:var(--white);font-size:11px;line-height:26px;text-decoration:none}
.foot-info{display:flex;align-items:center;gap:18px;color:var(--white);font-size:11px;height:34px;margin-bottom:16px}
.foot-info b{display:flex;align-items:center;justify-content:center;width:30px;height:30px;border-radius:50%;background:var(--white)}
.social{display:flex;gap:11px}
.social span{display:block;width:30px;height:30px;border-radius:50%;border:2px solid var(--white)}
.copyright{left:0;top:4798px;width:1200px;text-align:center;color:var(--white);font-size:10px}
</style>
</head>
<body>

<!-- navigation -->
<header class="abs nav">
  <div class="abs brand"><i></i>Coral Ridge</div>
  <nav class="abs menu">
    <span class="active">Home</span><span>About Us</span><span>Our Vaues</span><span>Our Services</span><span>Contact Us</span>
  </nav>
  <div class="abs phone-btn">1-555-310-2284</div>
</header>

<!-- hero -->
<section class="abs hero" role="img" aria-label="Rooftop telecom equipment cabinets and antenna masts with city and mountains behind">
</section>
<h1 class="abs" style="left:105px;top:198px;font-size:48px;line-height:77px;font-weight:700;width:660px">Neque in orci ac sit amet turpis ultrices sagittis.</h1>
<p class="abs" style="left:105px;top:354px;font-size:19px;line-height:30px;color:var(--ink);width:600px">Lorem ipsum dolor sit amet, consectetur adipiscing elit. At gravida justo, ut ut turpis nec faucibus. Lacus in lobortis</p>
<div class="abs btn" style="left:105px;top:463px;width:227px;height:51px">Contact Us</div>
<svg class="abs" style="left:0;top:640px" width="1200" height="66" viewBox="0 0 1200 66">
  <path d="M0 8 L600 50 L1200 8 L1200 66 L0 66 Z" fill="#ffffff"/>
  <path d="M0 8 L600 50 L1200 8 L1200 20 L600 66 L0 20 Z" fill="#3a5ca8"/>
</svg>

<!-- about -->
<section class="about">
  <div class="abs about-frame"></div>
  <div class="abs about-photo" role="img" aria-label="Telecom cabinets and antenna mounts on a rooftop under blue sky"></div>
  <h2 class="abs" style="left:566px;top:835px;font-size:36px;font-weight:900">About Us</h2>
  <div class="abs about-copy">
    <p>At Coral Ridge Ltd, we are dedicated to providing our customers with friendly professional service. We value your business. We have made it our mission to provide reliable products and services in our customer-driven approach.</p>
    <p>Our courteous, professional team is able to support a range of services to meet your requirements.</p>
    <p>To learn more about Coral Ridge Ltd, and the products and services we can offer, please call us at 1-555-310-2284.</p>
  </div>
</section>

<!-- services -->
<h2 class="section-title" style="top:1275px">Our Services</h2>
<div class="abs service" style="left:101px;top:1382px">
  <div class="photo" role="img" aria-label="Equipment shelters on a brick building rooftop" style="background:linear-gradient(160deg,#b8c3cf,#8a7566 55%,#c7c9cb)"></div>
  <h3>Rooftop Sites</h3>
  <p>Structural upgrades or simple ballast mounts. Shelter on the ground, leasehold build outs or cabinets on the roof.&nbsp; Coral Ridge can install what you need where you need it.</p>
</div>
<div class="abs divider" style="left:420px"></div>
<div class="abs service" style="left:456px;top:1382px">
  <div class="photo" role="img" aria-label="Transmission tower silhouetted against a purple dusk sky" style="background:linear-gradient(180deg,#2a2440,#5c4a6e 60%,#a07a8c)"></div>
  <h3>Towers and Monopoles</h3>
  <p>Coral Ridge can engineer, supply and install all your tower needs.&nbsp; New structures or existing, call us for pricing we would be happy to help out.</p>
</div>
<div class="abs divider" style="left:773px"></div>
<div class="abs service" style="left:808px;top:1382px">
  <div class="photo" role="img" aria-label="Glass office tower against a blue sky" style="background:linear-gradient(135deg,#4f86cf,#1f4f9c 55%,#6ea4e0)"></div>
  <h3>In Building</h3>
  <p>Small office or large Hotel.&nbsp; Coral Ridge has installed services into all size buildings.&nbsp; Fiber, cat6, or coax, we have the abilities to install, test, and get the job done.</p>
</div>

<!-- values -->
<section class="abs values" role="img" aria-label="Faded rooftop antenna installation in the background"></section>
<h2 class="section-title" style="top:1962px">Our Values</h2>
<svg class="abs" style="left:400px;top:2120px" width="400" height="300" viewBox="0 0 400 300">
  <polyline points="18,24 88,24 140,80" fill="none" stroke="#6b7790" stroke-width="1"/>
  <polyline points="382,24 312,24 260,80" fill="none" stroke="#6b7790" stroke-width="1"/>
  <polyline points="18,246 88,246 140,190" fill="none" stroke="#6b7790" stroke-width="1"/>
  <polyline points="382,246 312,246 260,190" fill="none" stroke="#6b7790" stroke-width="1"/>
</svg>
<div class="abs" role="img" aria-label="Rooftop cabinets and antennas" style="left:505px;top:2174px;width:190px;height:190px;transform:rotate(45deg);border-radius:18px;background:linear-gradient(135deg,#4f86cf,#9aa6b3 50%,#4a4c50)"></div>

<div class="abs value" style="left:101px;top:2076px">
  <svg width="46" height="40" viewBox="0 0 46 40" fill="none" stroke="#3a5ca8" stroke-width="2.5"><path d="M23 4v30M8 10h30M8 10l-6 14h12zM38 10l-6 14h12zM14 36h18"/></svg>
  <h3>Lorem ipsum dolor</h3>
  <p>Lorem ipsum dolor sit amet, consectetur adipiscing elit. Ut auctor semper at ante lacus, phasellus. In volutpat ornare lectus risus eget placerat eu egestas lacus.</p>
</div>
<div class="abs value" style="left:804px;top:2076px">
  <svg width="46" height="40" viewBox="0 0 46 40" fill="none" stroke="#3a5ca8" stroke-width="2.5"><path d="M14 14a9 9 0 0 1 18 0zM12 14h22M23 18a5 5 0 1 0 0.1 0M10 38c0-8 6-12 13-12s13 4 13 12z"/></svg>
  <h3>Lorem ipsum dolor</h3>
  <p>Lorem ipsum dolor sit amet, consectetur adipiscing elit. Ut auctor semper at ante lacus, phasellus. In volutpat ornare lectus risus eget placerat eu egestas lacus.</p>
</div>
<div class="abs value" style="left:101px;top:2300px">
  <svg width="46" height="40" viewBox="0 0 46 40" fill="none" stroke="#3a5ca8" stroke-width="2.5"><path d="M4 2v36h40M8 32l10-18 8 10 14-18M8 32l10-10 8 6 12-10"/></svg>
  <h3>Lorem ipsum dolor</h3>
  <p>Lorem ipsum dolor sit amet, consectetur adipiscing elit. Ut auctor semper at ante lacus, phasellus. In volutpat ornare lectus risus eget placerat eu egestas lacus.</p>
</div>
<div class="abs value" style="left:804px;top:2300px">
  <svg width="46" height="40" viewBox="0 0 46 40" fill="none" stroke="#3a5ca8" stroke-width="2.5"><path d="M23 2l16 6v12c0 10-7 16-16 18-9-2-16-8-16-18V8z"/><path d="M23 12l2.5 5 5.5.8-4 3.8 1 5.4-5-2.6-5 2.6 1-5.4-4-3.8 5.5-.8z" fill="#3a5ca8" stroke="none"/></svg>
  <h3>Lorem ipsum dolor</h3>
  <p>Lorem ipsum dolor sit amet, consectetur adipiscing elit. Ut auctor semper at ante lacus, phasellus. In volutpat ornare lectus risus eget placerat eu egestas lacus.</p>
</div>

<!-- trusted -->
<h2 class="section-title" style="top:2626px">Trusted By</h2>
<div class="abs partner" style="left:101px;top:2734px"><span></span></div>
<div class="abs partner" style="left:315px;top:2734px"><span></span></div>
<div class="abs partner" style="left:528px;top:2734px"><span></span></div>
<div class="abs partner" style="left:741px;top:2734px"><span></span></div>
<div class="abs partner" style="left:954px;top:2734px"><span></span></div>
<div class="abs partner" style="left:101px;top:2878px"><span></span></div>
<div class="abs partner" style="left:315px;top:2878px"><span></span></div>
<div class="abs partner" style="left:528px;top:2878px"><span></span></div>
<div class="abs partner" style="left:741px;top:2878px"><span></span></div>
<div class="abs partner" style="left:954px;top:2878px"><span></span></div>

<!-- why choose us -->
<section class="abs why" role="img" aria-label="Faded rooftop antenna site in the background"></section>
<h2 class="section-title" style="top:3152px">Why Choose Us</h2>
<p class="abs why-copy">At Coral Ridge Networks Ltd Safety is number one.&nbsp; Coral Ridge is committed to a strong safety policy, protecting its staff and the general public from accidents and harm.&nbsp; All Coral Ridge Employees are certified "Tower Competent Climber and Rescue" from the Veltrax Systems training program.<br>In addition to tower safety and fall protection Coral Ridge's safety training and practices include but are not limited to the following:</p>

<div class="abs check" style="left:182px;top:3396px"><svg width="28" height="28" viewBox="0 0 28 28" fill="none" stroke="#2b2f38" stroke-width="1.8"><circle cx="14" cy="14" r="12"/><path d="M8 14l5 5 11-12"/></svg>BC Level 1 first aid</div>
<div class="abs check" style="left:182px;top:3463px"><svg width="28" height="28" viewBox="0 0 28 28" fill="none" stroke="#2b2f38" stroke-width="1.8"><circle cx="14" cy="14" r="12"/><path d="M8 14l5 5 11-12"/></svg>Ascent Level 1</div>
<div class="abs check" style="left:182px;top:3531px"><svg width="28" height="28" viewBox="0 0 28 28" fill="none" stroke="#2b2f38" stroke-width="1.8"><circle cx="14" cy="14" r="12"/><path d="M8 14l5 5 11-12"/></svg>Monthly in office safety meetings</div>
<div class="abs check" style="left:613px;top:3396px"><svg width="28" height="28" viewBox="0 0 28 28" fill="none" stroke="#2b2f38" stroke-width="1.8"><circle cx="14" cy="14" r="12"/><path d="M8 14l5 5 11-12"/></svg>Transportation Endorsement first aid</div>
<div class="abs check" style="left:613px;top:3455px"><svg width="28" height="28" viewBox="0 0 28 28" fill="none" stroke="#2b2f38" stroke-width="1.8" style="flex:none"><circle cx="14" cy="14" r="12"/><path d="M8 14l5 5 11-12"/></svg>On site tailboard meeting with daily checklist sign off and picture documentation</div>
<div class="abs check" style="left:613px;top:3531px;width:460px"><svg width="28" height="28" viewBox="0 0 28 28" fill="none" stroke="#2b2f38" stroke-width="1.8"><circle cx="14" cy="14" r="12"/><path d="M8 14l5 5 11-12"/></svg>Job site specific hazard assessment and reporting</div>

<!-- contact -->
<h2 class="section-title" style="top:3719px">Contact Us</h2>
<div class="abs form-frame"></div>
<div class="abs info-card">
  <h3>Contact Info</h3>
  <div class="info-row" style="top:174px"><svg width="20" height="24" viewBox="0 0 20 24" fill="none" stroke="#fff" stroke-width="2"><path d="M10 22s8-8 8-13a8 8 0 0 0-16 0c0 5 8 13 8 13z"/><circle cx="10" cy="9" r="3"/></svg>415 Harbour Crest Rd, Fernvale, BC V0X1K7</div>
  <div class="info-row" style="top:237px"><svg width="20" height="24" viewBox="0 0 24 24" fill="#fff"><path d="M6.6 10.8a15.1 15.1 0 0 0 6.6 6.6l2.2-2.2a1 1 0 0 1 1-.25 11.4 11.4 0 0 0 3.6.57 1 1 0 0 1 1 1V20a1 1 0 0 1-1 1A17 17 0 0 1 3 4a1 1 0 0 1 1-1h3.5a1 1 0 0 1 1 1c0 1.25.2 2.45.57 3.57a1 1 0 0 1-.25 1z"/></svg>1-555-310-2284</div>
  <div class="info-row" style="top:300px"><svg width="22" height="18" viewBox="0 0 22 18" fill="none" stroke="#fff" stroke-width="2"><rect x="1" y="1" width="20" height="16" rx="2"/><path d="M1 3l10 7 10-7"/></svg>hello@coralridgenet.ca</div>
</div>
<h3 class="abs" style="left:645px;top:3898px;font-family:'Montserrat',sans-serif;font-size:28px;font-weight:500">Get In Touch</h3>
<div class="abs field" style="left:648px;top:4002px;width:156px">First Name</div>
<div class="abs field" style="left:864px;top:4002px;width:156px">Last Name</div>
<div class="abs field" style="left:645px;top:4067px;width:375px">Email Address</div>
<div class="abs field" style="left:645px;top:4133px;width:375px">Message</div>
<div class="abs btn" style="left:645px;top:4217px;width:229px;height:49px">Send</div>

<!-- footer -->
<svg class="abs" style="left:0;top:4421px" width="1200" height="406" viewBox="0 0 1200 406" preserveAspectRatio="none">
  <defs><linearGradient id="footGrad" x1="0" y1="0" x2="1" y2="0"><stop offset="0" stop-color="#5aa9dd"/><stop offset="0.55" stop-color="#4272bb"/><stop offset="1" stop-color="#2f4c8c"/></linearGradient></defs>
  <path d="M0 42 L600 0 L1200 42 L1200 406 L0 406 Z" fill="url(#footGrad)"/>
  <path d="M0 52 L600 14 L1200 52 L1200 60 L600 24 L0 60 Z" fill="#ffffff"/>
</svg>
<div class="abs foot-col" style="left:101px;top:4548px">
  <h4>Quick Links</h4>
  <a>Home</a><a>About Us</a><a>Our Values</a><a>Trusted By</a><a>Why Coose Us</a>
</div>
<div class="abs foot-col" style="left:330px;top:4548px">
  <h4>Services</h4>
  <a>Rooftop Sites</a><a>Towers and Monopoles</a><a>In Building</a>
</div>
<div class="abs foot-col" style="left:566px;top:4548px">
  <h4>Contact Info</h4>
  <div class="foot-info"><b><svg width="14" height="14" viewBox="0 0 24 24" fill="#3a5ca8"><path d="M6.6 10.8a15.1 15.1 0 0 0 6.6 6.6l2.2-2.2a1 1 0 0 1 1-.25 11.4 11.4 0 0 0 3.6.57 1 1 0 0 1 1 1V20a1 1 0 0 1-1 1A17 17 0 0 1 3 4a1 1 0 0 1 1-1h3.5a1 1 0 0 1 1 1c0 1.25.2 2.45.57 3.57a1 1 0 0 1-.25 1z"/></svg></b>1-555-310-2284</div>
  <div class="foot-info"><b><svg width="12" height="14" viewBox="0 0 20 24" fill="#3a5ca8"><path d="M10 23s9-9 9-14a9 9 0 0 0-18 0c0 5 9 14 9 14zm0-11a3 3 0 1 1 0-6 3 3 0 0 1 0 6z"/></svg></b>415 Harbour Crest Rd, Fernvale, BC V0X1K7</div>
  <div class="foot-info"><b><svg width="14" height="12" viewBox="0 0 22 18" fill="none" stroke="#3a5ca8" stroke-width="2.4"><rect x="1" y="1" width="20" height="16" rx="2"/><path d="M1 3l10 7 10-7"/></svg></b>hello@coralridgenet.ca</div>
</div>
<div class="abs foot-col" style="left:939px;top:4548px">
  <h4>Follow Us On</h4>
  <div class="social"><span></span><span></span><span></span><span></span></div>
</div>
<p class="abs copyright">Copyright 2017 Coral Ridge Ltd</p>

</body>
</html>
```